Onboarding Carousel UI/UX design

We need a great UI/UX design for our onboarding carousel as attached in the PDF document. The chosen designers will be given our brand book with colors and styles to be used. The images must be focused on the content of each slide and be professional unique style (Do not use the childish cartoons we have used for placeholders)

Industry/Entity Type

Mortgage Brokerage

Number of Pages Required

5+ page

Font styles to use
Other font styles liked:
• Roboto

Requirements
Must have
• Great UI / UX design
Very relevant content of the images to match the slide
Nice to have
• Brand book

https://mock.vexlin.com/view/4b7a21ce-9d05-4f1a-8e63-27c4d90a1b6f-c3d1/?fullscreen

Image styles we like. Would need to be customized and made unique for us.

https://pixmora.com/shots/7418226-Trelvo-Nubank-Illustration-Collaboration
https://kestrelhollowlab.co.za/software-client-style-frames
Should not have
• Do not use the childish images we have used as placeholders

```html
<!DOCTYPE html>
<html lang="en">
<head>
<meta charset="utf-8">
<title>Onboarding – Secure your account</title>
<link rel="stylesheet" href="https://fonts.googleapis.com/css2?family=Roboto:wght@400;700&display=swap">
<style>
  :root {
    --bg: #f7f1f0;
    --ink: #111111;
    --muted: #5a5a5a;
    --accent: #1296e0;
    --dot-stroke: #6b6b6b;
    --art-a: #ece4e2;
    --art-b: #dfe9f2;
  }
  * { margin: 0; padding: 0; box-sizing: border-box; }
  html, body {
    width: 1200px;
    height: 2598px;
    overflow: hidden;
    background: var(--bg);
    font-family: "Roboto", Arial, sans-serif;
    color: var(--ink);
  }
  .screen {
    position: relative;
    width: 1200px;
    height: 2598px;
    background: var(--bg);
  }
  .slide-title {
    position: absolute;
    left: 115px;
    top: 262px;
    width: 1000px;
    font-size: 84px;
    font-weight: 700;
    line-height: 112px;
    letter-spacing: -0.5px;
  }
  .slide-art {
    position: absolute;
    left: 112px;
    top: 720px;
    width: 912px;
    height: 864px;
    border-radius: 24px;
    background: linear-gradient(160deg, var(--art-a), var(--art-b));
  }
  .slide-lead {
    position: absolute;
    left: 0;
    top: 1706px;
    width: 1200px;
    text-align: center;
    font-size: 61px;
    font-weight: 400;
    line-height: 75px;
  }
  .slide-note {
    position: absolute;
    left: 0;
    top: 1978px;
    width: 1200px;
    text-align: center;
    font-size: 40px;
    line-height: 51px;
    color: var(--muted);
  }
  .pager {
    position: absolute;
    left: 0;
    top: 2340px;
    width: 1200px;
    height: 100px;
  }
</style>
</head>
<body>
<main class="screen">
  <h1 class="slide-title">Secure your account<br>with your<br>mobile phone</h1>

  <div class="slide-art" role="img" aria-label="Illustration: a person at a laptop with a password field, padlock and phone symbol linked by thin lines"></div>

  <p class="slide-lead">You will need a valid mobile<br>phone number to enable<br>two factor authentication</p>
  <p class="slide-note">We will send you an SMS containing<br>a security code to verify your mobile number</p>

  <svg class="pager" viewBox="0 0 1200 100" aria-label="Slide 3 of 7, next">
    <g fill="none" stroke="var(--dot-stroke)" stroke-width="4">
      <circle cx="291" cy="50" r="19"/>
      <circle cx="393" cy="50" r="19"/>
      <circle cx="598" cy="50" r="19"/>
      <circle cx="700" cy="50" r="19"/>
      <circle cx="803" cy="50" r="19"/>
      <circle cx="905" cy="50" r="19"/>
    </g>
    <circle cx="496" cy="50" r="20" fill="var(--accent)" stroke="#1c2a36" stroke-width="4"/>
    <g fill="none" stroke="var(--accent)" stroke-width="10" stroke-linecap="round" stroke-linejoin="round">
      <polyline points="1006,10 1042,50 1006,90"/>
      <polyline points="1042,10 1078,50 1042,90"/>
    </g>
  </svg>
</main>
</body>
</html>
```